Virtual Assistant/Online Marketing Business Card/Stationary

I need a professional but modern business card/stationary for my company in Dallas called Brivolo. Brivolo is a virtual assistant specializing in online marketing. I would like a unique design that stands out and makes my brand clear. Incorporating the logo is a must and have attached it to this brief.

Target Market(s)

small business owners & entrepreneurs, 35-65

Industry/Entity Type

Business

Contact Information for Business Card

Maren Tolk
marentolk@brivolo.biz
(555) 271-9064
brivolo.biz

Font styles to use
Sans Serif

Colors
f04a50
3176b5
9bcb3c

Requirements
Must have
• Colors that match the logo colors. Logo integration

```html
<!DOCTYPE html>
<html lang="en">
<head>
<meta charset="utf-8">
<title>Brivolo Stationery</title>
<link rel="stylesheet" href="https://fonts.googleapis.com/css2?family=Open+Sans:wght@400;600;700;800&display=swap">
<style>
  :root {
    --green: #b2bf5a;
    --orange: #e4654a;
    --blue: #336ea3;
    --ink: #111111;
    --paper: #ffffff;
    --backdrop: #ecebe8;
  }
  * { box-sizing: border-box; margin: 0; padding: 0; }
  html, body { width: 1200px; height: 1200px; overflow: hidden; }
  body {
    background: var(--backdrop);
    font-family: "Open Sans", sans-serif;
    color: var(--ink);
    position: relative;
  }
  .letterhead, .card {
    position: absolute;
    background: var(--paper);
    box-shadow: 0 2px 10px rgba(0,0,0,0.12);
    overflow: hidden;
  }
  .letterhead { left: 60px; top: 199px; width: 620px; height: 802px; }
  .wordmark {
    font-weight: 800;
    color: var(--ink);
    letter-spacing: -0.5px;
    line-height: 1;
  }
  .letterhead .wordmark {
    position: absolute; left: 44px; top: 58px; font-size: 38px;
  }
  .letterhead-stripes {
    position: absolute; left: 204px; right: 0; top: 72px;
  }
  .stripe { height: 8px; margin-bottom: 5px; }
  .stripe.green { background: var(--green); }
  .stripe.orange { background: var(--orange); height: 10px; }
  .stripe.blue { background: var(--blue); height: 7px; }
  .letterhead-footer {
    position: absolute; left: 44px; right: 44px; bottom: 38px;
    border-top: 3px solid var(--blue);
    padding-top: 8px;
    text-align: center;
    font-size: 15px;
  }
  .card { left: 740px; width: 400px; height: 229px; }
  .card-front { top: 330px; }
  .card-front .wordmark {
    position: absolute; left: 0; right: 0; top: 62px;
    text-align: center; font-size: 64px;
  }
  .tagline {
    position: absolute; left: 0; right: 0; top: 146px;
    text-align: center;
    color: var(--orange);
    font-weight: 600; font-size: 17px; letter-spacing: 4px;
  }
  .card-contact { top: 620px; }
  .card-contact .wordmark {
    position: absolute; left: 26px; top: 40px; font-size: 36px;
  }
  .card-name {
    position: absolute; right: 40px; top: 30px;
    font-weight: 700; font-size: 15px;
  }
  .contact-bands { position: absolute; left: 0; right: 0; bottom: 0; }
  .band {
    display: flex; align-items: center; justify-content: center; gap: 6px;
    font-size: 12px;
  }
  .band svg { width: 12px; height: 12px; flex: none; }
  .band.green { background: var(--green); height: 24px; }
  .band.orange { background: var(--orange); height: 30px; }
  .band.blue { background: var(--blue); height: 32px; color: #fff; font-weight: 700; }
</style>
</head>
<body>

<section class="letterhead">
  <div class="wordmark">Brivolo</div>
  <div class="letterhead-stripes">
    <div class="stripe green"></div>
    <div class="stripe orange"></div>
    <div class="stripe blue"></div>
  </div>
  <p class="letterhead-footer">12345 Main Street · Anytown · ST · 12345</p>
</section>

<section class="card card-front">
  <div class="wordmark">Brivolo</div>
  <p class="tagline">Online Marketing</p>
</section>

<section class="card card-contact">
  <div class="wordmark">Brivolo</div>
  <p class="card-name">Maren Tolk</p>
  <div class="contact-bands">
    <p class="band green">
      <svg viewBox="0 0 12 12" fill="none" stroke="currentColor" stroke-width="1"><rect x="0.5" y="2.5" width="11" height="7"/><path d="M0.5 2.5 6 7l5.5-4.5"/></svg>
      marentolk@brivolo.biz
    </p>
    <p class="band orange">
      <svg viewBox="0 0 12 12" fill="none" stroke="currentColor" stroke-width="1"><rect x="3" y="0.5" width="6" height="11" rx="1"/><line x1="5" y1="9.5" x2="7" y2="9.5"/></svg>
      (555) 271-9064
    </p>
    <p class="band blue">
      <svg viewBox="0 0 12 12" fill="none" stroke="currentColor" stroke-width="1"><circle cx="6" cy="6" r="5.5"/><ellipse cx="6" cy="6" rx="2.5" ry="5.5"/><line x1="0.5" y1="6" x2="11.5" y2="6"/></svg>
      www.brivolo.biz
    </p>
  </div>
</section>

</body>
</html>
```